International Property Consultancy

Brief Overview:

I need a dynamic and well designed website that is easy to use and understand. It has to be unique and different to generic templates that most websites seem to be these days. PLEASE NO GENERIC TEMPLATES FROM THE INTERNET.

Our business has 10 years experience working on struggling international developments that we then work in-house for to turn around and brings bout success. We stay within a project often for long periods of time until success is achieved. We are unique in our approach and completely different to the standard routes to market for many developments. The site is for developers to see what we have done in regards to previous projects, as such we want to incorporate video into this site with a strong design aesthetic. There will be videos of the past projects we have worked on, which will act as case studies.

I like very simple but punchy websites, that people can navigate and understand very easily. Also a big fan of unique and well thought out design aesthetic.

Initial Site layout thoughts:

1) Homepage:
2) About Us
3) What we've done / Work
This part has the projects we have worked on (France, Portugal, London, Morocco). Each one will have some video content and photo images, but also would be good to have a succinct way to mention what we did and the successes in a clever and punchy way.

4) Contact Us

* This is just a guideline. Would be open to input and creative direction on your own part.

*More details and websites we like can be seen in the brief doc attached.

PLEASE VIEW THE WIREFRAME WORD DOC ATTACHED.

Here there are also some more examples to help:

Here are just a few examples of websites and what I like about them:

- www.velmoro.com (clean, nice geometric design aesthetic, good animation when loading and changing pages well thought out all though also coulee be considered a bit dull and basic after the initial homepage slide)
- https://www.farbridgehub.net (Clean site, quite clinical, lacks video content and doesn't engage greatly).
- https://ruskotile.com (minimal, and like how it mixes the design aesthetic more with video and photo content)

- https://www.amberquillworks.com (like the layout of this and how it displays the projects and work section)

- https://brisk.com (Good use of video content)

- https://loomfield.studio (minimal to the point and mixes design with video and animation etc...)

Here is another couple of cool websites that may help give you some direction: https://halvenquay.com www.brisk.com

Hi there, One of the things I thought would be good on the homepage is to add the logo with a 'digital landscape' before flicking down into a slide with video content of the projects... Just an idea but have posted some pics in the brief. We would get this animated for the site. But if you have better ideas, please do run with them. Thanks,

Target Market(s)

Property developers

Number of Pages Required

4 page

Font styles to use
Other font styles liked:
• Read brief

Requirements
Must have
• Needs to be clean, dynamic and easy to follow on desktop and mobile. We will use it as a kind of portfolio website so will need to embed video of past projects we have worked on.

Read brief in docs.
Nice to have
• Clean
Should not have
• Not be another generic template website.
Not have random property stock photos. (We are not a property agency).

```html
<!DOCTYPE html>
<html lang="en">
<head>
<meta charset="utf-8">
<title>Talbrook Advisory — case study, about and contact pages</title>
<link href="https://fonts.googleapis.com/css2?family=Outfit:wght@300;400;500;600;700&display=swap" rel="stylesheet">
<style>
:root{
  --stage:#fdf4e9;
  --page:#ffffff;
  --ink:#1e2326;
  --muted:#7b7f83;
  --brand:#123f52;
  --rule:#e4e4e4;
  --link:#8a7be0;
}
*{box-sizing:border-box;margin:0;padding:0}
html,body{width:1200px;height:1029px;overflow:hidden}
body{background:var(--stage);font-family:"Outfit",sans-serif;color:var(--ink);position:relative}
.page{position:absolute;width:326px;background:var(--page);overflow:hidden;box-shadow:0 18px 40px rgba(140,110,60,.12)}
.page > *{position:absolute}
.brand-name{left:17px;top:11px;display:flex;align-items:center;gap:3px;font-size:5.6px;font-weight:600;color:var(--ink);letter-spacing:.6px;text-transform:uppercase}
.brand-name i{display:block;width:4px;height:4px;background:var(--ink)}
.nav{top:11px;font-size:3.6px;color:var(--brand)}
.nav.dim{color:var(--muted)}
.title{font-size:13px;font-weight:500;line-height:1}
.label{font-size:6.4px;font-weight:500}
.body{font-size:2.9px;line-height:5.2px;color:var(--muted);width:148px}
.quote{font-size:6.4px;line-height:11px;color:#55595d;width:146px}
.photo{overflow:hidden}
.caption{position:absolute;left:5px;bottom:6px;font-size:2.8px;font-weight:600;color:#fff}
.play{position:absolute;left:50%;top:50%;width:20px;height:20px;margin:-10px 0 0 -10px}
.progress{height:1px;background:var(--rule)}
.progress i{display:block;width:73px;height:1px;background:#9aa0a4}
.btn{height:12px;width:43px;background:var(--brand);color:#fff;font-size:3px;display:flex;align-items:center;justify-content:center;gap:3px}
.footer-copy{font-size:2.9px;color:var(--muted)}
.footer-mail{font-size:2.9px;color:var(--link)}
.socials{display:flex;gap:7px}
.socials span{width:4px;height:4px;border-radius:50%;background:#3a3f43;display:block}
.case-name{font-size:20px;font-weight:700;color:var(--brand);line-height:1}
.hello{font-size:19px;font-weight:500;line-height:24px}
.contact-line{font-size:4px;color:#44484c;line-height:5.4px}
</style>
</head>
<body>

<!-- Case study page: France -->
<section class="page" style="left:74px;top:41px;height:926px">
  <div class="brand-name"><i></i>Talbrook</div>
  <div class="nav" style="left:276px">About</div>
  <div class="nav" style="left:297px">Contact</div>
  <h1 class="title" style="left:17px;top:40px">France</h1>
  <p class="body" style="left:17px;top:58px;width:200px;font-size:3.8px">Augue eget nisi, turpis vel nibh urna, ut quam odio libero.</p>

  <div class="photo" role="img" aria-label="Project video still: wave-shaped perforated building facade against blue sky" style="left:17px;top:78px;width:292px;height:164px;background:linear-gradient(160deg,#2f7391 0%,#5f98b0 40%,#c9d6dc 75%,#eef1f2 100%)">
    <span style="position:absolute;left:0;right:0;top:66px;text-align:center;font-size:22px;font-weight:700;color:#fff">France</span>
    <svg class="play" viewBox="0 0 20 20"><circle cx="10" cy="10" r="10" fill="#2b2b2b"/><path d="M8 6.5v7l5.5-3.5z" fill="#fff"/></svg>
  </div>

  <h2 class="label" style="left:17px;top:278px">The challenge</h2>
  <p class="body" style="left:126px;top:277px">Augue eget nisi, turpis vel nibh urna, ut quam odio libero, aliquam, morbi proin feugiat nisl mattis enim venenatis nunc, malesuada urna, viverra massa lacus pellentesque lacus, tortor eleifend egestas vitae dignissim odio arcu nunc scelerisque nisl nunc gravida id egestas eros ullamcorper turpis orci id mattis ipsum sit adipiscing</p>

  <div class="photo" role="img" aria-label="White modular building facade" style="left:17px;top:320px;width:92px;height:64px;background:linear-gradient(180deg,#c7dbe6,#e9ecee 60%,#b8bfc4)"><span class="caption">Ac elit nisi, sem urna gravida</span></div>
  <div class="photo" role="img" aria-label="Glass building corner against teal gradient" style="left:17px;top:402px;width:92px;height:64px;background:linear-gradient(120deg,#1ec9b8,#1a6e78 55%,#0f3e4c)"><span class="caption">Ac elit nisi, sem urna gravida eget in nibh eleifend</span></div>
  <div class="photo" role="img" aria-label="Layered concrete balconies rising into blue sky" style="left:126px;top:320px;width:182px;height:146px;background:linear-gradient(160deg,#3f8fb8 0%,#8cbad3 35%,#d9d4cc 65%,#8c8680 100%)"><span class="caption">Ac elit nisi, sem urna gravida eget in nibh eleifend</span></div>

  <p class="quote" style="left:96px;top:499px">Augue eget nisi, turpis vel nibh urna, ut quam odio libero, aliquam, morbi proin feugiat nisl mattis enim venenatis nunc, malesuada urna, viverra massa lacus pellentesque lacus, tortor eleifend egestas vitae dignissim odio arcu nunc scelerisque nisl nunc gravida id egestas eros ullamcorper turpis orci id mattis ipsum sit adipiscing</p>

  <div class="photo" role="img" aria-label="Dark grey panelled building with sky" style="left:17px;top:623px;width:110px;height:81px;background:linear-gradient(135deg,#2a2f38,#555c66 60%,#9fb3c6)"></div>
  <div class="photo" role="img" aria-label="Facade of copper and black panels" style="left:144px;top:623px;width:110px;height:81px;background:linear-gradient(90deg,#1c2426,#a4583b 40%,#1c2426 60%,#b86a48)"></div>
  <div class="photo" role="img" aria-label="Timber slatted facade" style="left:271px;top:623px;width:55px;height:81px;background:linear-gradient(90deg,#b8835a,#3b3a38 50%,#c4956a)"></div>

  <div class="progress" style="left:17px;top:718px;width:292px"><i></i></div>

  <h2 class="label" style="left:17px;top:755px">Solution</h2>
  <p class="body" style="left:126px;top:754px">Augue eget nisi, turpis vel nibh urna, ut quam odio libero, aliquam, morbi proin feugiat nisl mattis enim venenatis nunc, malesuada urna, viverra massa lacus pellentesque lacus, tortor eleifend egestas vitae dignissim odio arcu nunc scelerisque nisl nunc gravida id egestas eros ullamcorper turpis orci id mattis ipsum sit adipiscing</p>

  <div class="photo" role="img" aria-label="Project video still: curved white amphitheatre building with warm lit opening" style="left:17px;top:797px;width:292px;height:129px;background:linear-gradient(180deg,#b9d9e2 0%,#e6e8e6 35%,#f2d7a8 55%,#dedcd8 75%,#cfcfcc 100%)">
    <svg class="play" viewBox="0 0 20 20"><circle cx="10" cy="10" r="10" fill="#2b2b2b"/><path d="M8 6.5v7l5.5-3.5z" fill="#fff"/></svg>
  </div>
</section>

<!-- Case study page: continued -->
<section class="page" style="left:437px;top:41px;height:924px">
  <div class="progress" style="left:17px;top:8px;width:292px"><i></i></div>

  <h2 class="label" style="left:17px;top:45px">Solution</h2>
  <p class="body" style="left:126px;top:44px">Augue eget nisi, turpis vel nibh urna, ut quam odio libero, aliquam, morbi proin feugiat nisl mattis enim venenatis nunc, malesuada urna, viverra massa lacus pellentesque lacus, tortor eleifend egestas vitae dignissim odio arcu nunc scelerisque nisl nunc gravida id egestas eros ullamcorper turpis orci id mattis ipsum sit adipiscing</p>

  <div class="photo" role="img" aria-label="Project video still: curved white amphitheatre building with warm lit opening" style="left:17px;top:86px;width:292px;height:164px;background:linear-gradient(180deg,#b9d9e2 0%,#e6e8e6 30%,#f2d7a8 45%,#e4e2de 62%,#cfcfcc 100%)">
    <svg class="play" viewBox="0 0 20 20"><circle cx="10" cy="10" r="10" fill="#2b2b2b"/><path d="M8 6.5v7l5.5-3.5z" fill="#fff"/></svg>
  </div>

  <p class="body" style="left:126px;top:269px">Proin neque lectus eu, porttitor sollicitudin sed ipsum et integer quam commodo quis sit volutpat lorem molestie sed aliquet sagittis fermentum amet, lobortis odio tempus id eleifend condimentum bibendum donec viverra dictum scelerisque in ultricies non, rhoncus volutpat quam risus blandit a egestas nunc sed nam nisl lectus vulputate eget bibendum justo enim malesuada suscipit egestas lacus blandit massa habitant mauris phasellus sociis vestibulum interdum tempor cursus semper malesuada neque amet, rhoncus, bibendum eu fringilla eu lacus libero nulla tellus pretium massa tortor neque purus feugiat mauris vitae dolor non metus, rhoncus ornare interdum in eget elit, tristique sed hendrerit</p>
  <p class="body" style="left:126px;top:340px">Massa vitae aliquam condimentum diam aliquam suspendisse diam in in egestas congue eget fringilla neque suspendisse diam, ultrices interdum tristique malesuada euismod justo, ipsum tristique volutpat magna condimentum lectus aliquet cras egestas amet duis pretium semper id suspendisse orci non</p>

  <div class="photo" role="img" aria-label="Dark metal-clad block with red trim against blue sky" style="left:17px;top:383px;width:92px;height:146px;background:linear-gradient(180deg,#3b8fcb 0%,#5aa0d0 30%,#3a3d42 55%,#272a2e 100%)"><span class="caption">Ac elit nisi, sem urna gravida eget in nibh eleifend</span></div>
  <div class="photo" role="img" aria-label="Red panelled building corner against blue sky" style="left:126px;top:383px;width:182px;height:146px;background:linear-gradient(160deg,#1a8fd6 0%,#1a8fd6 25%,#c8303c 50%,#8e1a24 100%)"><span class="caption">Ac elit nisi, sem urna gravida eget in nibh eleifend</span></div>

  <h2 class="label" style="left:17px;top:565px">Outcome</h2>
  <p class="body" style="left:126px;top:564px">Proin neque lectus eu, porttitor sollicitudin sed ipsum et integer quam commodo quis sit volutpat lorem molestie sed aliquet sagittis fermentum amet, lobortis odio tempus id eleifend condimentum bibendum donec viverra dictum scelerisque in ultricies non, rhoncus volutpat quam risus blandit a egestas nunc sed nam nisl lectus vulputate eget bibendum justo enim malesuada suscipit egestas lacus blandit mass.</p>

  <h2 class="title" style="left:17px;top:631px">More Case Studies</h2>

  <div class="photo" role="img" aria-label="Moroco project: glass tower with grid facade" style="left:31px;top:665px;width:109px;height:129px;background:linear-gradient(160deg,#7fa9c6,#c3d7e4 55%,#eef3f7)"></div>
  <div class="photo" role="img" aria-label="Portugal project: angular glass skyscraper" style="left:162px;top:665px;width:109px;height:129px;background:linear-gradient(180deg,#c8d6e0,#8fa6b6 60%,#d9e2e8)"></div>
  <div class="photo" role="img" aria-label="London project: pale stone building" style="left:292px;top:665px;width:34px;height:129px;background:linear-gradient(90deg,#c9cfd2,#9da6aa)"></div>
  <span class="case-name" style="left:17px;top:751px">Moroco</span>
  <span class="case-name" style="left:148px;top:751px">Portugal</span>
  <span class="case-name" style="left:279px;top:751px">London</span>

  <h2 class="title" style="left:17px;top:831px">Say hi,</h2>
  <p style="left:126px;top:830px;font-size:6.4px;line-height:11px;width:100px">We'd love to learn more about your project.</p>
  <div class="btn" style="left:126px;top:861px">Let's Talk <svg width="6" height="4" viewBox="0 0 6 4"><path d="M0 2h5M3.5.5 5 2 3.5 3.5" stroke="#fff" stroke-width=".5" fill="none"/></svg></div>

  <p class="footer-copy" style="left:17px;top:906px">Copyright © 2020 Talbrook</p>
  <p class="footer-mail" style="left:219px;top:906px">hello@talbrook.com</p>
  <div class="socials" style="left:271px;top:906px"><span></span><span></span><span></span><span></span></div>
</section>

<!-- About page -->
<section class="page" style="left:800px;top:41px;height:380px">
  <div class="brand-name"><i></i>Talbrook</div>
  <div class="nav dim" style="left:276px">About</div>
  <div class="nav" style="left:297px">Contact</div>
  <h1 class="title" style="left:17px;top:41px">About us</h1>
  <p class="body" style="left:146px;top:40px;width:108px">Augue eget nisi, turpis vel nibh urna, ut quam odio libero, aliquam, morbi proin feugiat nisl mattis enim venenatis nunc, malesuada urna, viverra massa lacus pellentesque lacus, tortor eleifend egestas vitae dignissim odio arcu nunc scelerisque nisl nunc gravida id egestas eros ullamcorper turpis orci id mattis ipsum sit adipiscing</p>
  <p class="body" style="left:146px;top:82px;width:108px">Massa vitae aliquam condimentum diam aliquam suspendisse diam in in egestas congue eget fringilla neque suspendisse diam, ultrices interdum tristique.</p>
  <p style="left:146px;top:115px;font-size:3.8px;color:var(--brand)">We'd love to learn more about your project.</p>
  <div class="btn" style="left:146px;top:131px">Let's Talk <svg width="6" height="4" viewBox="0 0 6 4"><path d="M0 2h5M3.5.5 5 2 3.5 3.5" stroke="#fff" stroke-width=".5" fill="none"/></svg></div>

  <h2 class="title" style="left:17px;top:181px">Meet our team</h2>
  <div class="photo" role="img" aria-label="Black and white portrait of a team member" style="left:17px;top:213px;width:109px;height:115px;background:linear-gradient(180deg,#9a9a9a,#5c5c5c 60%,#1d1d1d)"></div>
  <p style="left:140px;top:259px;font-size:10px;font-weight:500">Member Name</p>
  <p style="left:140px;top:276px;font-size:4px;color:#55595d">Ceo/Founder, Designation</p>
  <div class="photo" role="img" aria-label="Black and white portrait of a second team member" style="left:273px;top:213px;width:53px;height:115px;background:linear-gradient(90deg,#6e6e6e,#2a2a2a)"></div>

  <p class="footer-copy" style="left:17px;top:362px">Copyright © 2020 Talbrook</p>
  <p class="footer-mail" style="left:219px;top:362px">hello@talbrook.com</p>
  <div class="socials" style="left:271px;top:362px"><span></span><span></span><span></span><span></span></div>
</section>

<!-- Contact page -->
<section class="page" style="left:800px;top:450px;height:183px">
  <div class="brand-name"><i></i>Talbrook</div>
  <div class="nav" style="left:276px">About</div>
  <div class="nav dim" style="left:297px">Contact</div>
  <h1 class="hello" style="left:17px;top:40px">Hello<br>Bonjour<br>Olá<br>marhabaan</h1>
  <h2 style="left:200px;top:52px;font-size:6.4px;font-weight:500">Contact us</h2>
  <p class="contact-line" style="left:200px;top:71px">hello@talbrook.com</p>
  <p class="contact-line" style="left:200px;top:87px">+555 0192 47 31</p>
  <p class="contact-line" style="left:200px;top:103px">2481 Alder Row<br>Fenwick, Ohio<br>40215</p>

  <p class="footer-copy" style="left:17px;top:165px">Copyright © 2020 Talbrook</p>
  <p class="footer-mail" style="left:219px;top:165px">hello@talbrook.com</p>
  <div class="socials" style="left:271px;top:165px"><span></span><span></span><span></span><span></span></div>
</section>

</body>
</html>
```